Modern Informational OBGYN website

Looking for a modern Wordpress website for a general OBGYN practice in Florida with a specialty in High Risk Obstetrics. We had an old Joomla website that crashed and we lost most of the files. It was over 10 years old and needed a refresh anyway.

Our practice serves a multicultural patient population (white, black, Spanish and Indian) and we would like our website to reflect that diversity. Our company colors are sunshine yellow (#ECBF6D) often combined with black, white and steel blue (#7191BE) in the "life" part of our logo (attached) depending on the background. Our tagline is "We're specialist in You!" Overall the site should have a clean modern yet comfortable feel. One that portrays friendliness and competence. At least 6 pages (Home, Obstetrics, Gynecology, News, Patient Education and Resources). Rotating stock pictures or videos are fine for the headers of the pages if the design you're considering calls for it. Interesting and creative use of typography and icons are encouraged.

The home page should have a call to action to schedule an appointment as well as a link to our patient portal. Other than the home and news pages, the other pages should have a similar look and feel. The home page should have sections on "About Us", "Medical Staff" (with pictures and brief bio for 2 male doctors, 2 female midwives and 1 female nurse practitioner), "Services" and "Location". The news page will be a closed blog that will not allow comments or responses. Both the obstetrics and the gynecology pages will have an educational blurb on the respective topics followed by a list of our services for each topic. Would be nice on the obstetrics page to have information and graphics changes that occur during each trimester (but not necessary). The resource page will have sections on at least "Office Forms", Office Policies", "OB Guide" each with multiple downloadable PDF's. Also a section on "Insurance" with a list of all the major insurance plans that we take with links to their company websites. The address, link and map to our hospital and their website can also go on this page. The Patient Education Page can be broken into 3 sections Obstetrics, Gynecology which both will have definition of medical disorders followed by FAQ's and "Helpful Links" which would have links to other website for medical information.

That's all that I can think of right now. The above is to help guide you but I am flexible, if the website design dictates a better flow of information. Looking forward to seeing what you can come up with. Down the road, I will be looking to the winning designer to produce matching brochures, full, half and quarter page media ads to have on hand for the practices further needs.

Target Market(s)

Women looking medical services

Industry/Entity Type

Medical

Coding

Coded - Design and coding required

Number of Pages Required

5+ page

Font styles to use
Sans Serif
Script

Colors

Designer to choose colors to be used in the design.

Requirements
Must have
• None. See projects description for suggestions
Nice to have
• infographics like information on stages of pregnancy on the obstetrics page

```html
<!DOCTYPE html>
<html lang="en">
<head>
<meta charset="utf-8">
<title>Dawnlight Women's Care</title>
<link href="https://fonts.googleapis.com/css2?family=Poppins:wght@400;500;600;700&family=Great+Vibes&display=swap" rel="stylesheet">
<style>
:root{
  --sun:#ECBF6D;
  --sun-deep:#F2A93B;
  --sun-bright:#F6B928;
  --steel:#7191BE;
  --ink:#222222;
  --text:#555555;
  --muted:#8a8a8a;
  --soft:#f3f3f5;
  --white:#ffffff;
  --dark:#1d1d1d;
}
*{box-sizing:border-box;margin:0;padding:0}
html,body{width:1200px;height:4540px;overflow:hidden}
body{font-family:"Poppins",Arial,sans-serif;color:var(--text);background:var(--white);position:relative}
.abs{position:absolute}
.script{font-family:"Great Vibes",cursive;color:var(--sun-deep);font-size:34px;line-height:1}
.section-title{font-size:40px;font-weight:600;color:var(--ink);letter-spacing:1px}
.section-title b{color:var(--sun-deep);font-weight:600}
.btn{display:inline-block;border-radius:30px;font-size:13px;font-weight:600;letter-spacing:.5px;text-transform:uppercase;padding:14px 30px;color:var(--white)}
.btn-sun{background:var(--sun-bright)}
.btn-steel{background:var(--steel)}
.link-more{font-size:11px;font-weight:600;color:var(--ink);text-transform:uppercase;border-bottom:2px solid var(--sun-bright);padding-bottom:2px}

/* header */
.site-header{position:absolute;top:0;left:0;width:1200px;height:70px;z-index:5;display:flex;align-items:center;padding:0 40px}
.brand{display:flex;align-items:center;gap:10px;font-size:24px;font-weight:700;color:var(--sun-deep)}
.brand-dot{width:26px;height:26px;border-radius:50%;background:var(--sun-bright)}
.main-nav{display:flex;gap:34px;margin-left:70px;font-size:12px;font-weight:600;color:var(--ink)}
.main-nav .active{color:var(--sun-deep);border-bottom:2px solid var(--sun-bright);padding-bottom:4px}
.portal{margin-left:40px;background:var(--steel);color:#fff;font-size:11px;font-weight:600;padding:10px 20px;border-radius:20px}
.lang{margin-left:14px;font-size:11px;font-weight:600;border:1px solid #ccc;border-radius:14px;padding:6px 12px;color:var(--ink);background:#fff}

/* hero */
.hero{position:absolute;top:0;left:0;width:1200px;height:640px}
.hero-photo{position:absolute;left:0;top:0;width:1200px;height:600px;background:linear-gradient(100deg,#f7f3ee 0%,#efe7de 35%,#d9c7b8 60%,#c8d3df 100%)}
.hero-copy{position:absolute;left:100px;top:270px;width:520px;z-index:2}
.hero-copy h1{font-size:32px;font-weight:700;color:var(--ink);margin:6px 0 12px;white-space:nowrap}
.hero-copy p{font-size:17px;line-height:1.45;color:var(--ink);margin-bottom:24px;width:440px}
.hero-arrow{position:absolute;top:330px;width:20px;height:40px}
.hero-wave{position:absolute;left:0;top:510px;z-index:1}

/* about */
.about-photo{left:120px;top:660px;width:440px;height:620px;background:radial-gradient(circle at 55% 40%,#d9b8a4 0%,#f3ded2 35%,#fbf6f2 70%,#ffffff 100%)}
.about-copy{left:600px;top:800px;width:470px}
.about-copy p{font-size:14px;line-height:1.75;margin:20px 0 30px}

/* services */
.services{top:1330px;left:0;width:1200px;height:560px;background:var(--soft)}
.services-head{top:1400px;left:0;width:1200px;text-align:center}
.svc-circle{left:445px;top:1490px;width:310px;height:310px;border-radius:50%;border:8px solid #fff;box-shadow:0 0 0 2px var(--sun);background:linear-gradient(135deg,#e8d8ce,#c9d6e6)}
.svc{width:290px}
.svc h3{font-size:16px;font-weight:600;color:var(--ink);margin-bottom:8px}
.svc p{font-size:12px;line-height:1.6;margin-bottom:8px}
.svc-icon{width:70px;height:70px;border-radius:50%;background:var(--sun-bright);display:flex;align-items:center;justify-content:center;border:4px solid #fff;box-shadow:0 0 0 2px var(--sun);flex:none}

/* staff */
.staff{top:1870px;left:0;width:1200px;height:1030px;background:linear-gradient(180deg,var(--sun-bright),var(--sun) 60%,var(--sun-bright))}
.staff-head{top:2000px;left:0;width:1200px;text-align:center}
.staff-head .script{color:#fff}
.staff-head .section-title{color:#fff}
.card{width:280px;height:290px;border:2px solid #fff;border-radius:8px;text-align:center;color:#fff;padding:110px 24px 0}
.card.featured{background:#fff;color:var(--text);height:310px}
.card h3{font-size:20px;font-weight:600;margin-bottom:8px}
.card.featured h3{color:var(--ink)}
.card p{font-size:11px;line-height:1.6;margin-bottom:12px}
.card .link-more{color:inherit;border-color:#fff}
.card.featured .link-more{color:var(--ink);border-color:var(--sun-bright)}
.avatar{position:absolute;left:80px;top:-50px;width:120px;height:120px;border-radius:50%;border:5px solid #fff;background:linear-gradient(160deg,#f1e6dc,#c8b3a2)}

/* blogs */
.blogs-head{top:2960px;left:0;width:1200px;text-align:center}
.blog{width:290px;height:330px;background:#fff;box-shadow:0 6px 20px rgba(0,0,0,.08);border-radius:6px;overflow:hidden}
.blog-img{height:170px}
.blog-tag{position:absolute;left:16px;top:160px;background:var(--sun-bright);color:#fff;font-size:10px;font-weight:600;padding:4px 12px;border-radius:3px}
.blog-body{padding:24px 18px 0}
.blog-body h3{font-size:15px;font-weight:600;color:var(--ink);margin-bottom:8px}
.blog-body p{font-size:11px;line-height:1.6;margin-bottom:10px}

/* location */
.location{left:140px;top:3660px;width:340px}
.location .section-title{font-size:36px}
.location p{font-size:14px;line-height:1.6;margin:14px 0 40px}
.loc-row{display:flex;align-items:center;gap:16px;font-size:14px;color:var(--ink);margin-bottom:26px}
.loc-ico{width:38px;height:38px;border-radius:50%;background:var(--sun-bright);display:flex;align-items:center;justify-content:center;flex:none}
.map{left:500px;top:3630px;width:590px;height:330px;border-radius:6px;background:linear-gradient(135deg,#ececec,#dcdcdc)}

/* footer */
.footer{top:4180px;left:0;width:1200px;height:360px;background:var(--dark);color:#cfcfcf}
.foot-col{top:4250px;color:#cfcfcf}
.foot-col h4{font-size:13px;font-weight:600;color:#fff;text-transform:uppercase;margin-bottom:16px;padding-left:10px;border-left:3px solid var(--sun-bright)}
.foot-col li{list-style:none;font-size:12px;line-height:2}
.foot-brand{font-size:26px;font-weight:700;color:var(--sun-bright);display:flex;align-items:center;gap:10px}
.socials{display:flex;gap:8px;margin-top:14px}
.socials span{width:26px;height:26px;border-radius:50%;background:#fff;display:block}
.contact-row{display:flex;gap:12px;align-items:center;margin-bottom:16px;font-size:12px}
.contact-row b{display:block;color:#fff;font-size:13px}
.copyright{top:4500px;left:0;width:1200px;text-align:center;font-size:11px;color:#aaa;border-top:1px solid #333;padding-top:12px}
.copyright b{color:var(--sun-bright);font-weight:500}
</style>
</head>
<body>

<section class="hero">
  <div class="hero-photo" role="img" aria-label="Photo of a smiling doctor caring for a pregnant patient"></div>
  <svg class="hero-arrow" style="left:20px" viewBox="0 0 20 40"><path d="M16 4 4 20l12 16" fill="none" stroke="#999" stroke-width="2"/></svg>
  <svg class="hero-arrow" style="right:20px" viewBox="0 0 20 40"><path d="M4 4l12 16L4 36" fill="none" stroke="#999" stroke-width="2"/></svg>
  <div class="hero-copy">
    <div class="script" style="font-size:38px">Welcome to Dawnlight</div>
    <h1>WE'RE SPECIALIST IN YOU!</h1>
    <p>At Dawnlight our obstetrics providers and staff are dedicated supporting</p>
    <span class="btn btn-sun">Schedule an appointment</span>
  </div>
  <svg class="hero-wave" width="1200" height="130" viewBox="0 0 1200 130" preserveAspectRatio="none">
    <path d="M0 70C250 40 420 120 700 80S1050 20 1200 40V130H0Z" fill="var(--sun-bright)"/>
    <path d="M0 95C260 70 440 130 720 105S1050 60 1200 75V130H0Z" fill="#fff"/>
  </svg>
</section>

<header class="site-header">
  <div class="brand"><span class="brand-dot"></span>Dawnlight</div>
  <nav class="main-nav">
    <span class="active">OBSTETRICS</span><span>GYNECOLOGY</span><span>NEWS</span><span>PATIENT EDUCATION</span><span>RESOURCES</span>
  </nav>
  <span class="portal">PATIENT PORTAL</span>
  <span class="lang">ENG ▾</span>
</header>

<div class="abs about-photo" role="img" aria-label="Photo of a smiling pregnant woman holding her belly"></div>
<div class="abs about-copy">
  <div class="script">Who we are</div>
  <div class="section-title">ABOUT <b>DAWNLIGHT</b></div>
  <p>Lorem Ipsum is simply dummy text of the printing and typesetting industry. Lorem Ipsum has been the industry's standard dummy text ever since simply dummy text of the printing and typesetting industry. Lorem Ipsum has been the industry's standard dummy text ever since when an unknown printer took a galley of type and scrambled it to make a type specimen book. It has survived not only five centuries, but also the leap.</p>
  <span class="btn btn-steel">Learn more</span>
</div>

<div class="abs services"></div>
<svg class="abs" style="left:0;top:1300px" width="1200" height="60" viewBox="0 0 1200 60" preserveAspectRatio="none"><path d="M0 40C300 0 700 60 1200 20V60H0Z" fill="var(--soft)"/></svg>
<div class="abs services-head">
  <div class="script">What we do</div>
  <div class="section-title">OUR <b>SERVICES</b></div>
</div>
<div class="abs svc-circle" role="img" aria-label="Photo of a pregnant patient with her doctor"></div>

<div class="abs svc" style="left:120px;top:1510px;display:flex;gap:18px;align-items:flex-start">
  <div><h3>Prenatal &amp; Postpartum</h3><p>Lorem Ipsum is simply dummy text of the printing and typesetting industry.</p><span class="link-more">Learn more</span></div>
  <div class="svc-icon"><svg width="30" height="30" viewBox="0 0 30 30"><path d="M15 26s-10-6-10-13a5 5 0 0 1 10-2 5 5 0 0 1 10 2c0 7-10 13-10 13z" fill="none" stroke="#fff" stroke-width="2"/></svg></div>
</div>
<div class="abs svc" style="left:120px;top:1700px;display:flex;gap:18px;align-items:flex-start">
  <div><h3>Pregnancy Care</h3><p>Lorem Ipsum is simply dummy text of the printing and typesetting industry.</p><span class="link-more">Learn more</span></div>
  <div class="svc-icon"><svg width="30" height="30" viewBox="0 0 30 30"><circle cx="15" cy="15" r="9" fill="none" stroke="#fff" stroke-width="2"/><path d="M15 10v10M10 15h10" stroke="#fff" stroke-width="2"/></svg></div>
</div>
<div class="abs svc" style="left:790px;top:1510px;display:flex;gap:18px;align-items:flex-start">
  <div class="svc-icon"><svg width="30" height="30" viewBox="0 0 30 30"><circle cx="15" cy="12" r="6" fill="none" stroke="#fff" stroke-width="2"/><path d="M15 18v9M11 23h8" stroke="#fff" stroke-width="2"/></svg></div>
  <div><h3>Reproduction Health</h3><p>Lorem Ipsum is simply dummy text of the printing and typesetting industry.</p><span class="link-more">Learn more</span></div>
</div>
<div class="abs svc" style="left:790px;top:1700px;display:flex;gap:18px;align-items:flex-start">
  <div class="svc-icon"><svg width="30" height="30" viewBox="0 0 30 30"><path d="M8 6h14v18H8z" fill="none" stroke="#fff" stroke-width="2"/><path d="M11 12h8M11 16h8M11 20h5" stroke="#fff" stroke-width="2"/></svg></div>
  <div><h3>Gynecology</h3><p>Lorem Ipsum is simply dummy text of the printing and typesetting industry.</p><span class="link-more">Learn more</span></div>
</div>

<div class="abs staff" role="img" aria-label="Soft golden background"></div>
<svg class="abs" style="left:0;top:1840px" width="1200" height="90" viewBox="0 0 1200 90" preserveAspectRatio="none"><path d="M0 50C300 0 600 90 900 50S1100 20 1200 40V0H0Z" fill="var(--soft)"/></svg>
<svg class="abs" style="left:0;top:2860px" width="1200" height="80" viewBox="0 0 1200 80" preserveAspectRatio="none"><path d="M0 40C300 80 700 0 1200 40V80H0Z" fill="#fff"/></svg>
<div class="abs staff-head">
  <div class="script">Meet the team</div>
  <div class="section-title">MEDICAL STAFF</div>
</div>

<div class="abs card" style="left:132px;top:2170px"><div class="avatar" role="img" aria-label="Portrait of a male doctor"></div><h3>Male Doctor</h3><p>Lorem Ipsum is simply dummy text of the printing and typesetting industry.</p><span class="link-more">Learn more</span></div>
<div class="abs card featured" style="left:460px;top:2150px"><div class="avatar" role="img" aria-label="Portrait of a male doctor"></div><h3>Male Doctor</h3><p>Lorem Ipsum is simply dummy text of the printing and typesetting industry.</p><span class="link-more">Learn more</span></div>
<div class="abs card" style="left:788px;top:2170px"><div class="avatar" role="img" aria-label="Portrait of a female doctor"></div><h3>Female Doctor</h3><p>Lorem Ipsum is simply dummy text of the printing and typesetting industry.</p><span class="link-more">Learn more</span></div>
<div class="abs card" style="left:296px;top:2540px"><div class="avatar" role="img" aria-label="Portrait of a female doctor"></div><h3>Female Doctor</h3><p>Lorem Ipsum is simply dummy text of the printing and typesetting industry.</p><span class="link-more">Learn more</span></div>
<div class="abs card" style="left:624px;top:2540px"><div class="avatar" role="img" aria-label="Portrait of a nurse practitioner"></div><h3>Nurse Practitioner</h3><p>Lorem Ipsum is simply dummy text of the printing and typesetting industry.</p><span class="link-more">Learn more</span></div>

<div class="abs blogs-head">
  <div class="script">Have a look</div>
  <div class="section-title">RECENT <b>BLOGS</b></div>
</div>
<article class="abs blog" style="left:132px;top:3090px"><div class="blog-img" role="img" aria-label="Photo of a pregnant woman" style="background:linear-gradient(135deg,#5a4a44,#c9b6a8)"></div><span class="blog-tag">Obstetrics</span><div class="blog-body"><h3>Lorem ipsum dolor sit</h3><p>Duis aute irure dolor in reprehenderit in voluptate velit esse cillum dolore eu fugiat in culpa officia.</p><span class="link-more">Learn more</span></div></article>
<article class="abs blog" style="left:455px;top:3090px"><div class="blog-img" role="img" aria-label="Photo of a pregnant belly close up" style="background:linear-gradient(135deg,#c7d3e0,#f0e4da)"></div><span class="blog-tag">Pregnancy</span><div class="blog-body"><h3>Lorem ipsum dolor sit</h3><p>Duis aute irure dolor in reprehenderit in voluptate velit esse cillum dolore eu fugiat in culpa officia.</p><span class="link-more">Learn more</span></div></article>
<article class="abs blog" style="left:778px;top:3090px"><div class="blog-img" role="img" aria-label="Photo of an ultrasound examination" style="background:linear-gradient(135deg,#b9c4cf,#e6ddd6)"></div><span class="blog-tag">Gynecology</span><div class="blog-body"><h3>Lorem ipsum dolor sit</h3><p>Duis aute irure dolor in reprehenderit in voluptate velit esse cillum dolore eu fugiat in culpa officia.</p><span class="link-more">Learn more</span></div></article>

<div class="abs location">
  <div class="section-title">OUR <b>LOCATION</b></div>
  <p>Lorem Ipsum is simply dummy text of the printing and typesetting industry.</p>
  <div class="loc-row"><span class="loc-ico"><svg width="18" height="18" viewBox="0 0 18 18"><path d="M9 17s-6-6-6-10a6 6 0 0 1 12 0c0 4-6 10-6 10z" fill="#fff"/><circle cx="9" cy="7" r="2" fill="var(--sun-bright)"/></svg></span>480 Palm Grove Ave,<br>Lakewood, FL 33801</div>
  <div class="loc-row"><span class="loc-ico"><svg width="18" height="18" viewBox="0 0 18 18"><path d="M4 2l3 1 1 4-2 1a9 9 0 0 0 4 4l1-2 4 1 1 3-2 2C8 16 2 10 2 4z" fill="#fff"/></svg></span>(555) 014 2288</div>
</div>
<div class="abs map" role="img" aria-label="Street map showing the office location">
  <svg class="abs" style="left:275px;top:130px" width="40" height="52" viewBox="0 0 40 52"><path d="M20 50S4 30 4 18a16 16 0 0 1 32 0c0 12-16 32-16 32z" fill="var(--sun-bright)"/><circle cx="20" cy="18" r="6" fill="#fff"/></svg>
</div>

<div class="abs footer"></div>
<svg class="abs" style="left:0;top:4150px" width="1200" height="70" viewBox="0 0 1200 70" preserveAspectRatio="none"><path d="M0 20C300 60 800 0 1200 30V70H0Z" fill="var(--sun-bright)"/><path d="M0 40C320 70 800 20 1200 45V70H0Z" fill="var(--dark)"/></svg>
<div class="abs foot-col" style="left:120px;width:250px">
  <div class="foot-brand"><span class="brand-dot"></span>Dawnlight</div>
  <p style="font-size:11px;line-height:1.6;margin-top:12px">Lorem ipsum dolor sit amet, consectetur adipiscing elit, sed do eiusmod tempor incididunt ut labore.</p>
  <div class="socials"><span></span><span></span><span></span><span></span></div>
</div>
<div class="abs foot-col" style="left:430px"><h4>Navigation</h4><ul><li>Home</li><li>Obstetrics</li><li>Gynecology</li><li>News</li></ul></div>
<div class="abs foot-col" style="left:620px"><h4>Resources</h4><ul><li>Patient Education</li><li>Resources</li><li>Patient Portal</li><li>Contact Us</li></ul></div>
<div class="abs foot-col" style="left:860px">
  <h4>Contact Us</h4>
  <div class="contact-row"><span class="loc-ico" style="width:30px;height:30px"><svg width="14" height="14" viewBox="0 0 18 18"><path d="M4 2l3 1 1 4-2 1a9 9 0 0 0 4 4l1-2 4 1 1 3-2 2C8 16 2 10 2 4z" fill="#fff"/></svg></span><div>Phone number<b>(555) 018 3340</b></div></div>
  <div class="contact-row"><span class="loc-ico" style="width:30px;height:30px"><svg width="14" height="14" viewBox="0 0 16 16"><rect x="1" y="3" width="14" height="10" fill="none" stroke="#fff" stroke-width="1.6"/><path d="M1 3l7 6 7-6" fill="none" stroke="#fff" stroke-width="1.6"/></svg></span><div>Email us<b>hello@dawnlightcare.com</b></div></div>
</div>
<div class="abs copyright">Copyright © 2022 <b>Dawnlight</b> All Right Reserved.</div>

</body>
</html>
```